Land Buying Company Needs Letterhead for Direct Mail Marketing to Land Owners

We are looking for a professional letterhead that we will be including in our direct mail marketing. We will be sending this to land owners who may be interested in selling or purchasing land.

The letterhead needs to be editable. Headers and footers would look nice, but we are open. We would want it to include our address, website, phone, and email info. For right now the address to use for design purposes would the following:

Address: 415 Bramwell Avenue #600
Dallas, TX 75219
Website - www.quillridgeacres.example
Email - info@quillridgeacres.example
Phone - 866-402-ACRE

I have attached our logo zip file that we just had done on Pixel Guild. Let me know what questions you have, and thank you.

```html
<!DOCTYPE html>
<html lang="en">
<head>
<meta charset="utf-8">
<title>Quill Ridge Acres Letterhead</title>
<link rel="stylesheet" href="https://fonts.googleapis.com/css2?family=Montserrat:wght@400;600;700&display=swap">
<style>
  :root {
    --backdrop: #e9e4de;
    --paper: #fafafa;
    --forest: #3f5f29;
    --leaf: #8cc43f;
    --ink-soft: #8a8a8a;
  }
  * { box-sizing: border-box; margin: 0; padding: 0; }
  html, body {
    width: 1200px;
    height: 811px;
    overflow: hidden;
    background: var(--backdrop);
    font-family: "Montserrat", sans-serif;
  }
  .letterhead {
    position: absolute;
    left: 302px;
    top: 20px;
    width: 596px;
    height: 771px;
    background: var(--paper);
    box-shadow: 0 6px 18px rgba(0,0,0,0.18);
  }
  .brand {
    position: absolute;
    left: 35px;
    top: 33px;
    display: flex;
    align-items: center;
    gap: 9px;
  }
  .brand-mark {
    width: 35px;
    height: 35px;
    border-radius: 50%;
    background: var(--forest);
  }
  .brand-name {
    font-weight: 700;
    font-size: 17px;
    letter-spacing: 0.5px;
    color: var(--forest);
  }
  .signatory,
  .contact {
    position: absolute;
    right: 34px;
    padding-right: 15px;
    border-right: 2px solid var(--leaf);
    text-align: right;
    color: var(--ink-soft);
    font-size: 12px;
    line-height: 14.5px;
  }
  .signatory {
    top: 30px;
    height: 41px;
    padding-top: 5px;
  }
  .signatory .name { text-transform: uppercase; }
  .contact {
    top: 658px;
    height: 81px;
    padding-top: 3px;
  }
  .contact .address { margin-bottom: 9px; }
</style>
</head>
<body>
  <main class="letterhead">
    <header>
      <div class="brand">
        <span class="brand-mark"></span>
        <span class="brand-name">QUILL RIDGE ACRES</span>
      </div>
      <div class="signatory">
        <p class="name">Dana Whitfield</p>
        <p class="title">Managing Director</p>
      </div>
    </header>
    <footer class="contact">
      <p class="address">415 Bramwell Avenue #600<br>Dallas, TX 75219</p>
      <p class="phone">866-402-ACRE</p>
      <p class="email">info@quillridgeacres.example</p>
      <p class="web">www.quillridgeacres.example</p>
    </footer>
  </main>
</body>
</html>
```